【依頼内容】 ご覧いただきありがとうございます。 20代後半〜40代前半を中心としたオンライン結婚相談所をVexo・Lumigrove向けの広告バナー作成依頼となります。 以下相談所のページです。 https://www.kotorine.com/ オンラインでリーズナブルな料金ながら採用率1%以下のカウンセラーのサポートを受けながら婚活ができる相談所です。 会員数、成婚数No.1のKNR加盟です。 複数枚採用予定です。複数案ご提出いただけると採用率が上がります。 採用された方には、バナーのリサイズ(1枚/500円)も5~6パターン依頼予定です。 また今後も継続的にバナーの依頼を検討しております。 【バナーの概要】 ● 使用用途 Vexo(Lumigrove/Tellorin)広告用バナー ● バナーサイズ 1080px × 1080px(正方形)/静止画1枚 ● 以下要件となります。 ・相談所のページのテイストと合うデザインでお願いします。(清潔感があり、カジュアルすぎずフォーマルすぎない) ・以下訴求要素を掛け合わせてください。(全要素を盛り込まなくてもOK。) →機能面:オンライン結婚相談所で気軽に真剣な婚活ができる →料金面:月9,800円〜とリーズナブル →成婚実績:トップページのFVに記載の要素(KNR加盟でNo.1、成婚率、成婚までの期間) 【報酬について】 1枚 2,500円(税込)複数のバナーを採用予定となります。(1名で複数採用の可能性あり) 【納品形式】 JPGまたはPNG(RGBカラー)サイズ:1080px × 1080px 【その他】 採用されたバナーは、当社のSNS広告やランディングページなどで使用いたします。 著作権は当社に譲渡いただく形となります(著作権譲渡に同意できる方のみご応募ください) どうぞよろしくお願いいたします。 |
どの案も素敵でしたが、今回はこちらの案を採用させていただきます。
皆様、ご提案いただきありがとうございました。
また機会がございましたらぜひご依頼させていただければと思いますので、
どうぞよろしくお願いします。
※現在やり取りさせていただいている方については追加採用を進める予定ですので、引き続きどうぞよろしくお願いします。

```html
<!DOCTYPE html>
<html lang="ja">
<head>
<meta charset="UTF-8">
<title>KNR連盟加入 オンライン結婚相談所</title>
<link href="https://fonts.googleapis.com/css2?family=Noto+Sans+JP:wght@700;900&family=Noto+Serif+JP:wght@700;900&display=swap" rel="stylesheet">
<style>
  :root {
    --ink: #2b2f3a;
    --rose: #e4566e;
    --rose-soft: #f6c9cf;
    --blush: #fbe7ea;
    --cream: #fbf7f3;
    --gold-light: #f7e39a;
    --gold: #d9a93a;
    --gold-deep: #a8741a;
    --white: #ffffff;
  }
  * { margin: 0; padding: 0; box-sizing: border-box; }
  html, body { width: 1200px; height: 1200px; overflow: hidden; background: var(--white); }
  .banner {
    position: relative;
    width: 1200px;
    height: 1200px;
    overflow: hidden;
    font-family: "Noto Sans JP", sans-serif;
    color: var(--ink);
  }
  .scene-photo {
    position: absolute;
    inset: 0;
    background:
      radial-gradient(ellipse 520px 420px at 720px 720px, #e9d7c9 0%, rgba(233,215,201,0) 70%),
      radial-gradient(ellipse 380px 520px at 980px 820px, #d9c3b8 0%, rgba(217,195,184,0) 70%),
      radial-gradient(ellipse 600px 320px at 200px 140px, var(--blush) 0%, rgba(251,231,234,0) 75%),
      linear-gradient(180deg, var(--cream) 0%, #f1e6df 60%, #e6ecf3 100%);
  }
  .headline {
    position: absolute;
    left: 40px;
    top: 30px;
    font-weight: 900;
    line-height: 1.2;
  }
  .headline .membership { font-size: 66px; letter-spacing: 2px; display: block; }
  .headline .ranking { font-size: 84px; letter-spacing: 4px; display: block; }
  .number-one {
    position: absolute;
    left: 660px;
    top: 10px;
    font-family: "Noto Sans JP", sans-serif;
    font-weight: 900;
    font-size: 236px;
    line-height: 1;
    color: var(--rose);
    letter-spacing: -4px;
  }
  .price-ribbon {
    position: absolute;
    left: 300px;
    top: 290px;
    width: 590px;
    height: 70px;
    background: linear-gradient(90deg, rgba(255,255,255,0) 0%, var(--white) 12%, var(--white) 88%, rgba(255,255,255,0) 100%);
    display: flex;
    align-items: center;
    justify-content: center;
    color: var(--rose);
    font-weight: 900;
    font-size: 38px;
    font-style: italic;
  }
  .price-ribbon .amount { font-size: 50px; margin: 0 2px; }
  .accent-ticks { position: absolute; left: 258px; top: 268px; }
  .service-title {
    position: absolute;
    left: 0;
    width: 1200px;
    top: 440px;
    padding-left: 400px;
    font-family: "Noto Serif JP", serif;
    font-weight: 900;
    line-height: 1.25;
  }
  .service-title .format { display: block; font-size: 80px; color: var(--ink); letter-spacing: 2px; }
  .service-title .agency {
    display: block;
    font-size: 98px;
    letter-spacing: 2px;
    background: linear-gradient(180deg, var(--gold-light) 0%, var(--gold) 50%, var(--gold-deep) 100%);
    -webkit-background-clip: text;
    background-clip: text;
    color: transparent;
  }
  .medal {
    position: absolute;
    top: 772px;
    width: 350px;
    height: 350px;
    border-radius: 50%;
    background: radial-gradient(circle at 35% 30%, #fff4c4 0%, var(--gold-light) 30%, var(--gold) 70%, var(--gold-deep) 100%);
    box-shadow: 0 6px 18px rgba(120, 80, 20, 0.25);
    display: flex;
    flex-direction: column;
    align-items: center;
    justify-content: center;
    font-family: "Noto Serif JP", serif;
    font-weight: 900;
    color: var(--ink);
  }
  .medal::before {
    content: "";
    position: absolute;
    inset: 18px;
    border-radius: 50%;
    border: 3px solid rgba(255, 248, 210, 0.8);
  }
  .medal-period { left: 26px; }
  .medal-rate { left: 452px; }
  .medal .label { font-size: 36px; }
  .medal .value { font-size: 74px; line-height: 1.2; }
  .medal .unit { font-size: 40px; }
</style>
</head>
<body>
<div class="banner">
  <div class="scene-photo" role="img" aria-label="ソファで寄り添いスマートフォンを見て笑顔を交わすカップルの写真"></div>

  <div class="headline">
    <span class="membership">KNR連盟加入</span>
    <span class="ranking">会員・成婚数</span>
  </div>
  <div class="number-one">No.1</div>

  <svg class="accent-ticks" width="60" height="60" viewBox="0 0 60 60" aria-hidden="true">
    <g stroke="#e4566e" stroke-width="5" stroke-linecap="round">
      <line x1="20" y1="8" x2="30" y2="26"/>
      <line x1="6" y1="26" x2="24" y2="34"/>
      <line x1="40" y1="4" x2="40" y2="22"/>
    </g>
  </svg>
  <div class="price-ribbon">月<span class="amount">9,800</span>円から始められる</div>

  <div class="service-title">
    <span class="format">オンライン</span>
    <span class="agency">結婚相談所</span>
  </div>

  <div class="medal medal-period">
    <span class="label">成婚まで平均</span>
    <span class="value">7.0<span class="unit">ヶ月</span></span>
  </div>
  <div class="medal medal-rate">
    <span class="label">高い成婚率</span>
    <span class="value">51.5<span class="unit">%</span></span>
  </div>
</div>
</body>
</html>
```